automatic Real Estate Sales Brochure

Print-out of 3 to 8 pages automatically on a color inkjet printer. Page size A4
All details for my Real Estate Sales Design Project are in attached file.
Here some points:
We have abound 100 real estate objects for sale (houses, flats and pieces of land).
For each item, our system creates automatically a sales documentation, which we print out and hand to the potential buyers after they've visited the object or send it by mail upon request in form of a pdf.
This document should be of 3 to maximum 8 pages.
It should be of a modern design and invite the client to read it.
The information should be clear and quick to find.
If the global look could somehow relate to the look of our web site www.norvelhaus.ch, that would be nice.
The company data is there for legal reasons, but it is the agent's phone and mail that the clients should use for contact.
The photos should be of big size (2 by page?) without being distorted nor cut.
Optionally, to save ink and pages, maybe only the first 3-4 photos full size and the rest smaller?

Target Market(s)

will be printed or sent as PDF "on the fly", meaning no pre-printing at a print shop!

Industry/Entity Type

Real Estate

Font styles to use
Sans Serif

Requirements
Must have
• see details in attached file
Should not have
• no edge-to-edge printing
• no double-page printing (A3)

```html
<!DOCTYPE html>
<html lang="fr">
<head>
<meta charset="utf-8">
<title>Norvelhaus – Fiche de vente</title>
<link href="https://fonts.googleapis.com/css2?family=Open+Sans:wght@400;700&display=swap" rel="stylesheet">
<style>
  :root {
    --ink: #5b5959;
    --ink-dark: #4a4848;
    --band: #5f5d5d;
    --red: #ff0000;
    --paper: #ffffff;
    --backdrop: #e6e6e6;
    --rule: #8a8888;
  }
  * { margin: 0; padding: 0; box-sizing: border-box; }
  html, body { width: 1200px; height: 1200px; overflow: hidden; }
  body {
    background: var(--backdrop);
    font-family: "Open Sans", Arial, sans-serif;
    color: var(--ink);
    position: relative;
  }
  .sheet {
    position: absolute;
    left: 197px; top: 30px;
    width: 806px; height: 1140px;
    background: var(--paper);
    box-shadow: 0 4px 18px rgba(0,0,0,.18);
    overflow: hidden;
  }
  .agent {
    position: absolute; left: 45px; top: 50px;
    width: 330px; padding-bottom: 6px;
    border-bottom: 1.5px solid var(--ink);
    font-size: 16px; line-height: 20px;
  }
  .agent .agent-name { font-weight: 700; }
  .brand {
    position: absolute; right: 46px; top: 44px;
    display: flex; align-items: center; gap: 12px;
    font-size: 50px; font-weight: 700; line-height: 56px;
    color: var(--ink-dark); letter-spacing: -1px;
  }
  .brand-square { width: 30px; height: 30px; background: var(--red); }
  .photo { position: absolute; }
  .photo-garden {
    left: 0; top: 144px; width: 806px; height: 312px;
    background: linear-gradient(180deg, #6fb3ea 0%, #a9d2ef 30%, #4f7a34 55%, #3d6a27 80%, #6b8a3e 100%);
  }
  .photo-living {
    left: 0; top: 456px; width: 403px; height: 313px;
    background: linear-gradient(180deg, #f1eeee 0%, #e7e2e0 45%, #c98d3a 70%, #b9782a 100%);
  }
  .photo-bedroom {
    left: 403px; top: 456px; width: 403px; height: 313px;
    background: linear-gradient(90deg, #fff3d2 0%, #f6e5b4 40%, #3b3634 62%, #2a2727 100%);
  }
  .location-band {
    position: absolute; left: 0; top: 769px;
    width: 806px; height: 46px; background: var(--band);
  }
  .location-band svg { position: absolute; left: 0; top: 0; }
  .location {
    position: absolute; left: 45px; top: 6px;
    color: #fff; font-size: 28px; font-weight: 700; line-height: 34px;
  }
  .headline {
    position: absolute; left: 45px; top: 832px;
    font-size: 25px; font-weight: 700; color: var(--ink);
  }
  .tagline {
    position: absolute; left: 45px; top: 866px;
    font-size: 21px; color: var(--ink);
  }
  .facts {
    position: absolute; top: 907px;
    width: 335px; border-collapse: collapse;
    font-size: 16px; line-height: 23px;
  }
  .facts td { border-bottom: 1px solid var(--rule); padding: 0 0 0 1px; }
  .facts td:first-child { width: 229px; }
  .facts-left { left: 45px; }
  .facts-right { left: 426px; }
  .footer {
    position: absolute; left: 0; top: 1048px;
    width: 806px; height: 92px; background: var(--band);
    color: #fff; font-size: 16px; line-height: 19px;
  }
  .footer .col { position: absolute; top: 27px; }
  .footer .col-company { left: 45px; }
  .footer .col-company strong { font-weight: 700; }
  .footer .col-web { left: 371px; }
  .footer .col-phone { left: 621px; }
</style>
</head>
<body>
  <article class="sheet">
    <header>
      <div class="agent">
        <div class="agent-name">Elise Moreau</div>
        <div class="agent-contact">moreau@norvelhaus.ch | 077 480 16 29</div>
      </div>
      <div class="brand">
        <span class="brand-square"></span>
        <span class="brand-name">norvelhaus</span>
      </div>
    </header>

    <div class="photo photo-garden" role="img" aria-label="Jardin arboré avec grands arbres et façade blanche de l'immeuble"></div>
    <div class="photo photo-living" role="img" aria-label="Séjour lumineux avec cuisine ouverte et parquet"></div>
    <div class="photo photo-bedroom" role="img" aria-label="Chambre avec parquet et grande armoire à portes coulissantes"></div>

    <div class="location-band">
      <svg width="806" height="46" viewBox="0 0 806 46" aria-hidden="true">
        <polygon points="550,0 806,0 806,46 530,46" fill="var(--red)"/>
      </svg>
      <div class="location">1200 Genève</div>
    </div>

    <h1 class="headline">Lumineux 4.5 de 100m2 idéalement situé</h1>
    <p class="tagline">Spécialiste romand de vente immobilière</p>

    <table class="facts facts-left">
      <tr><td>Type de bien</td><td>Appartement</td></tr>
      <tr><td>Surface habitable m2</td><td>100m2</td></tr>
      <tr><td>Nombre de pièces</td><td>Pièces 4.5</td></tr>
      <tr><td>Surface parcelle m2</td><td>1'000m2</td></tr>
    </table>
    <table class="facts facts-right">
      <tr><td>Prix</td><td>CHF 910'000.-</td></tr>
      <tr><td>Année de</td><td>1994</td></tr>
      <tr><td>Etat</td><td>bon état</td></tr>
      <tr><td>Disponible</td><td>à convenir</td></tr>
    </table>

    <footer class="footer">
      <div class="col col-company"><strong>Norvelhaus Sàrl</strong><br>Rue des Vergers 7, 1096 Cully</div>
      <div class="col col-web">info@norvelhaus.ch<br>www.norvelhaus.ch</div>
      <div class="col col-phone">Tél. 021 845 17 40<br>Fax. 021 845 17 41</div>
    </footer>
  </article>
</body>
</html>
```